Business Card Design

I have a very clear idea of what I want. I just do not know how to do the graphic design to match it.

On the front I want the uploaded image with the horse and the two people.
I want

Bottom left hand corner
Lewis Brand
0438 512 607

Bottom right
There is maroon block with Neil Patton Practitioner Group Logo
Next to that I want the Stable Arc tile about the same size ( attached psd file)

On the back I want a plain colour (white) with the information

Lewis Brand
Equine Performance
Rowland4Ponies and Acupuncture
Horsemanship Lessons and Clinics
Horse Training

lbrand@fauna812.com.au
FB/lewis.brand.207
StableArc.com.au

Industry/Entity Type

Business

Contact Information for Business Card

Lewis Brand
0438 512 607
lbrand@fauna812.com.au

```html
<!DOCTYPE html>
<html lang="en">
<head>
<meta charset="utf-8">
<title>Stable Arc – Business Card</title>
<link href="https://fonts.googleapis.com/css2?family=Cinzel:wght@500&family=Open+Sans:wght@400;600;700&family=Yellowtail&family=Kaushan+Script&display=swap" rel="stylesheet">
<style>
  :root {
    --backdrop: #cfcfcf;
    --sand-light: #dcbd88;
    --sand-mid: #c9a36a;
    --sand-dark: #a98450;
    --brown: #4a2210;
    --maroon: #6b2a15;
    --navy: #0f3566;
    --paper: #f7f7f8;
    --charcoal: #333436;
    --white: #ffffff;
  }
  * { box-sizing: border-box; margin: 0; padding: 0; }
  html, body { width: 1200px; height: 1005px; overflow: hidden; }
  body { background: var(--backdrop); position: relative; font-family: "Open Sans", sans-serif; }

  .card {
    position: absolute;
    left: 260px;
    width: 680px;
    height: 389px;
    overflow: hidden;
    box-shadow: 0 6px 16px rgba(0,0,0,0.22);
  }
  .card--front { top: 92px; }
  .card--back { top: 522px; background: var(--paper); }

  /* Front */
  .front-photo {
    position: absolute; inset: 0;
    background:
      radial-gradient(ellipse at 70% 45%, rgba(80,50,25,0.25), transparent 45%),
      linear-gradient(160deg, var(--sand-light), var(--sand-mid) 55%, var(--sand-dark));
  }
  .headline { position: absolute; left: 70px; top: 66px; color: var(--brown); }
  .headline__lead {
    font-family: "Cinzel", serif; font-size: 21px; letter-spacing: 1px;
    transform: rotate(-8deg); transform-origin: left bottom; display: block;
  }
  .headline__your {
    font-family: "Yellowtail", cursive; font-size: 34px;
    position: absolute; left: 170px; top: 32px;
  }
  .headline__main {
    font-family: "Yellowtail", cursive; font-size: 96px; line-height: 1;
    position: absolute; left: 20px; top: 62px; transform: rotate(-8deg); white-space: nowrap;
  }
  .front-contact { position: absolute; left: 36px; bottom: 34px; color: var(--brown); }
  .front-contact__name { font-family: "Kaushan Script", cursive; font-size: 34px; line-height: 1.1; }
  .front-contact__phone { font-weight: 700; font-size: 20px; letter-spacing: 1px; }
  .partner-badge {
    position: absolute; right: 130px; bottom: 36px; width: 72px; height: 72px;
    background: var(--maroon); border: 2px solid #8a4a25;
  }
  .brand-tile {
    position: absolute; right: 42px; bottom: 44px; width: 72px; height: 72px;
    background: var(--white); border-radius: 12px;
    box-shadow: 0 8px 0 #5a2c14, 0 10px 10px rgba(0,0,0,0.3);
  }

  /* Back */
  .back-shapes { position: absolute; inset: 0; }
  .brand { position: absolute; left: 110px; top: 168px; display: flex; align-items: center; gap: 12px; color: var(--navy); }
  .brand__dot { width: 22px; height: 22px; border-radius: 50%; background: var(--navy); }
  .brand__name { font-weight: 700; font-size: 34px; }
  .back-name { position: absolute; left: 380px; top: 56px; font-family: "Kaushan Script", cursive; font-size: 40px; color: var(--navy); }
  .contact-list { position: absolute; left: 384px; top: 128px; list-style: none; color: var(--navy); font-size: 17px; }
  .contact-list li { display: flex; align-items: center; gap: 14px; margin-bottom: 6px; }
  .contact-list svg { width: 18px; height: 18px; fill: var(--navy); flex: none; }
  .social { position: absolute; left: 140px; top: 296px; display: flex; align-items: center; gap: 8px; color: var(--navy); font-size: 17px; }
  .social__mark { width: 14px; height: 14px; background: var(--navy); border-radius: 2px; }
  .services { position: absolute; left: 392px; top: 270px; color: var(--white); font-size: 16px; line-height: 1.3; }
</style>
</head>
<body>
  <section class="card card--front">
    <div class="front-photo" role="img" aria-label="Photo of a trainer in a hat watching a bay horse led on a rope by a woman across a sandy arena"></div>
    <div class="headline">
      <span class="headline__lead">How you ever gonna know</span>
      <span class="headline__your">Your</span>
      <span class="headline__main">Potential</span>
    </div>
    <div class="front-contact">
      <p class="front-contact__name">Lewis Brand</p>
      <p class="front-contact__phone">0438 512 607</p>
    </div>
    <div class="partner-badge" role="img" aria-label="Neil Patton Practitioner Group badge"></div>
    <div class="brand-tile" role="img" aria-label="Stable Arc tile"></div>
  </section>

  <section class="card card--back">
    <svg class="back-shapes" viewBox="0 0 680 389" preserveAspectRatio="none" aria-hidden="true">
      <polygon points="0,366 330,366 322,389 0,389" fill="var(--charcoal)"/>
      <polygon points="352,258 680,212 680,389 322,389" fill="var(--navy)"/>
    </svg>
    <div class="brand"><span class="brand__dot"></span><span class="brand__name">Stable Arc</span></div>
    <h1 class="back-name">Lewis Brand</h1>
    <ul class="contact-list">
      <li><svg viewBox="0 0 24 24"><path d="M6.6 10.8a15 15 0 0 0 6.6 6.6l2.2-2.2a1 1 0 0 1 1-.25 11.4 11.4 0 0 0 3.6.6 1 1 0 0 1 1 1V20a1 1 0 0 1-1 1A17 17 0 0 1 3 4a1 1 0 0 1 1-1h3.5a1 1 0 0 1 1 1c0 1.25.2 2.45.6 3.6a1 1 0 0 1-.25 1z"/></svg>0438 512 607</li>
      <li><svg viewBox="0 0 24 24"><path d="M12 2a10 10 0 1 0 0 20 10 10 0 0 0 0-20zm6.9 6h-2.9a15.7 15.7 0 0 0-1.4-3.6A8 8 0 0 1 18.9 8zM12 4c.8 1.2 1.5 2.5 1.9 4h-3.8c.4-1.5 1.1-2.8 1.9-4zM4.3 14a8 8 0 0 1 0-4h3.4a16.5 16.5 0 0 0 0 4zm.8 2H8c.3 1.3.8 2.5 1.4 3.6A8 8 0 0 1 5.1 16zM8 8H5.1a8 8 0 0 1 4.3-3.6C8.8 5.5 8.3 6.7 8 8zm4 12c-.8-1.2-1.5-2.5-1.9-4h3.8c-.4 1.5-1.1 2.8-1.9 4zm2.3-6H9.7a14.7 14.7 0 0 1 0-4h4.6a14.7 14.7 0 0 1 0 4zm.3 5.6c.6-1.1 1.1-2.3 1.4-3.6h2.9a8 8 0 0 1-4.3 3.6zm1.7-5.6a16.5 16.5 0 0 0 0-4h3.4a8 8 0 0 1 0 4z"/></svg>StableArc.com.au</li>
      <li><svg viewBox="0 0 24 24"><path d="M2 5h20v14H2zm2 2v.5l8 5 8-5V7zm0 2.8V17h16V9.8l-8 5z"/></svg>lbrand@fauna812.com.au</li>
    </ul>
    <div class="social"><span class="social__mark"></span>/lewis.brand.207</div>
    <div class="services">
      <p>Rowland4Ponies &amp; Acupuncture</p>
      <p>Horsemanship Lessons and Clinics</p>
      <p>Equine Performance &nbsp;• Horse Training</p>
    </div>
  </section>
</body>
</html>
```